Creative - Appealing - Business Card Design Project

Looking for a Business card design (vector artwork) for an existing company called 'Fernway Sound'. We operate in the entertainment industry specializing in audio system design and rental, however; we also deal with other sectors of the entertainment industry including lighting, video, staging and power system design and rental. We would like to see designs that don't focus too much on audio but include elements encompassing everything else.

Double sided business card, following our new colour scheme and logo, which is attached. The card would ideally be creative and eye catching to draw in new customers in the elegant event production market, such as weddings & corporate affairs.

Target Market(s)

High end corporate clients, wedding clients

Industry/Entity Type

Entertainment

Requirements
Must have
• Our contact details, these can be worded & listed however you think appropriate as part as the design

Business Name - Fernway Sound
My Name - Dominic Harwell
Web Address - www.fernwaysound-example.com
Mobile Number - 07914 362 517
Office Number - 0330 481 7265
Email - dom@fernwaysound-example.com

The name, email and mobile number would need to be able to be changed to my business partners also.

The font used on our logo is Sansation
Nice to have
• On one side maybe a word cloud involving the services in which we can provide; Lighting, Sound, Event Production, Staging, LED Uplighting, Projection Mapping, Wedding Hire

On the other side, all the important credentials of contact.
Should not have
• The design should not use any old style fonts (i.e Times New Roman, Gothic etc) or on the other side of the scale, any 'jokey' fonts (i.e. Comic Sans).

The font to be used is Sansation

```html
<!DOCTYPE html>
<html lang="en">
<head>
<meta charset="utf-8">
<title>Fernway Sound – Business Card</title>
<link rel="stylesheet" href="https://fonts.googleapis.com/css2?family=Sansation:wght@400;700&display=swap">
<style>
  :root {
    --stage: #e9e8ec;
    --purple-light: #8a639d;
    --purple: #6a3a86;
    --purple-deep: #4a2a5e;
    --grey-text: #333333;
    --grey-mark: #8c8c8c;
    --rule: #9a9a9a;
    --white: #ffffff;
  }
  * { box-sizing: border-box; margin: 0; padding: 0; }
  html, body { width: 1200px; height: 900px; overflow: hidden; }
  body {
    background: var(--stage);
    font-family: "Sansation", "Trebuchet MS", sans-serif;
    position: relative;
  }
  .card {
    position: absolute;
    top: 305px;
    width: 520px;
    height: 290px;
    box-shadow: 0 3px 8px rgba(0,0,0,0.25);
  }
  .card-front {
    left: 65px;
    background: linear-gradient(180deg, var(--purple-light) 0%, var(--purple) 45%, var(--purple-deep) 100%);
    color: var(--white);
  }
  .card-back {
    left: 615px;
    background: var(--white);
  }
  .service-list {
    position: absolute;
    left: 29px;
    top: 132px;
    font-size: 10px;
    line-height: 14px;
    letter-spacing: 0.2px;
  }
  .front-wordmark {
    position: absolute;
    left: 330px;
    top: 160px;
    width: 160px;
    text-align: center;
    font-weight: 700;
    color: var(--white);
  }
  .wordmark-dot {
    display: block;
    width: 46px;
    height: 46px;
    border-radius: 50%;
    background: var(--white);
    margin: -70px auto 22px;
  }
  .wordmark-line1 { display: block; font-size: 27px; line-height: 28px; }
  .wordmark-line2 { display: block; font-size: 16px; line-height: 20px; }

  .back-wordmark {
    position: absolute;
    left: 22px;
    top: 218px;
    width: 160px;
    text-align: center;
    font-weight: 700;
    color: var(--purple);
  }
  .back-wordmark .wordmark-dot { background: var(--purple); margin: -90px auto 42px; width: 56px; height: 56px; }

  .contact {
    position: absolute;
    right: 28px;
    top: 74px;
    width: 265px;
    text-align: right;
    color: var(--grey-text);
  }
  .contact-name { font-size: 17px; font-weight: 700; color: var(--purple); line-height: 20px; }
  .contact-role { font-size: 14px; line-height: 18px; margin-bottom: 10px; }
  .rule { border: 0; border-top: 1px solid var(--rule); margin: 0 0 10px; }
  .contact-row {
    display: flex;
    justify-content: flex-end;
    align-items: center;
    gap: 5px;
    font-size: 13.5px;
    line-height: 16px;
  }
  .contact-group { margin-bottom: 9px; }
  .contact-row svg { width: 11px; height: 11px; fill: var(--purple); flex: none; }
</style>
</head>
<body>
  <section class="card card-front" aria-label="Card front">
    <p class="service-list">
      Lighting • Sound • Event Production • Staging<br>
      LED Uplighting • Projection Mapping • Wedding Hire
    </p>
    <div class="front-wordmark">
      <span class="wordmark-dot"></span>
      <span class="wordmark-line1">FERNWAY</span>
      <span class="wordmark-line2">SOUND</span>
    </div>
  </section>

  <section class="card card-back" aria-label="Card back">
    <div class="back-wordmark">
      <span class="wordmark-dot"></span>
      <span class="wordmark-line1">FERNWAY</span>
      <span class="wordmark-line2">SOUND</span>
    </div>

    <div class="contact">
      <p class="contact-name">Dominic Harwell</p>
      <p class="contact-role">managing director</p>
      <hr class="rule">
      <div class="contact-group">
        <p class="contact-row">07914 362 517
          <svg viewBox="0 0 12 12" aria-hidden="true"><path d="M3 0h6a1 1 0 0 1 1 1v10a1 1 0 0 1-1 1H3a1 1 0 0 1-1-1V1a1 1 0 0 1 1-1zm0.5 1.5v7.5h5V1.5z"/></svg>
        </p>
        <p class="contact-row">0330 481 7265
          <svg viewBox="0 0 12 12" aria-hidden="true"><path d="M2.5 0.5l2 2.4-1 1.4c.6 1.6 2 3 3.6 3.6l1.4-1 2.4 2-1.2 2.2C5 10.6 1.4 7 .4 1.7z"/></svg>
        </p>
      </div>
      <hr class="rule">
      <p class="contact-row">dom@fernwaysound-example.com
        <svg viewBox="0 0 12 12" aria-hidden="true"><path d="M0 2h12v8H0zm1 1v.4l5 3.2 5-3.2V3z"/></svg>
      </p>
      <p class="contact-row">www.fernwaysound-example.com
        <svg viewBox="0 0 12 12" aria-hidden="true"><path d="M6 0a6 6 0 1 0 0 12A6 6 0 0 0 6 0zm-.5 1.1v2.4H3.6c.4-1.3 1.1-2.2 1.9-2.4zm1 0c.8.2 1.5 1.1 1.9 2.4H6.5zM1.3 4.5h2.1a9 9 0 0 0 0 3H1.3a5 5 0 0 1 0-3zm3.1 0h1.1v3H4.4a8 8 0 0 1 0-3zm2.1 0h1.1a8 8 0 0 1 0 3H6.5zm2.1 0h2.1a5 5 0 0 1 0 3H8.6a9 9 0 0 0 0-3zM3.6 8.5h1.9v2.4c-.8-.2-1.5-1.1-1.9-2.4zm2.9 0h1.9c-.4 1.3-1.1 2.2-1.9 2.4z"/></svg>
      </p>
    </div>
  </section>
</body>
</html>
```